flyer/brochure design to deliver to homes (letter box delivery)

Hi I would like something designed to represent my business Hair & Make up, I have a home based salon but offer mobile services for weddings. I really like beachy colours elegant and not to busy. but open to all different designs.

I will be getting these printed up through Tolvane Press the product specs are:

Document Trim Size
Horizontal
216 x 139 mm
2556 x 1642 pixels
Vertical
139 x 216 mm
1642 x 2556 pixels

Full Bleed Size
Horizontal
219 x 142 mm
2592 x 1677 pixels
Vertical
142 x 219 mm
1677 x 2592 pixels
Finished artwork should use the full bleed dimensions for best results.

I will also upload a recent business card that i have but dont have to stick to similar design

Reason: To give u more time

Industry/Entity Type

Salon

Requirements
Must have
• my logo (you can change the colour of my logo if you like)

would like it to have somewhere:
"look good feel great without paying silly prices"

must also have:

private home salon based in bateau bay, mobile service provided for weddings only

Im thinking I would like the price list on the back but open to what ever you submit

price list:
Ladies Cut $20
Ladies Blowdry $20 from
Mens cut $15
Full head of Foils, Toner, Cut & Blowdry $110
Half Head of Foils, Toner, Cut & Blowdry $80
Tint cut & colour $60-80
Tint with scattered foils Cut & Blowdry $70-$110

Wedding Package Hair & Make up $135pp mobile servive provided
check out our webpage for our complete pricelist

prices subject to change without notice

business details:

p: 0491 826 374
E: lcs@quorvel.com.au
W: www.lumencrestsalon.com.au

I would like it to have maybe on the front as an initial eye catcher:

Full head of foils, Toner, Cut & Blowdry $110 every day

```html
<!DOCTYPE html>
<html lang="en">
<head>
<meta charset="utf-8">
<title>Lumencrest Salon – Flyer</title>
<link rel="stylesheet" href="https://fonts.googleapis.com/css2?family=Pinyon+Script&family=Raleway:wght@300;500&family=Cinzel:wght@600&display=swap">
<style>
  :root {
    --paper: #ffffff;
    --photo-light: #f4f1ee;
    --photo-warm: #e6c79a;
    --photo-skin: #efc6ad;
    --orange: #f4915a;
    --rust: #c1602a;
    --rust-dark: #94421a;
    --ink: #1f1511;
  }
  * { margin: 0; padding: 0; box-sizing: border-box; }
  html, body {
    width: 779px;
    height: 1200px;
    overflow: hidden;
    background: var(--paper);
  }
  .flyer {
    position: relative;
    width: 779px;
    height: 1200px;
    overflow: hidden;
    background: var(--orange);
  }
  .hero-photo {
    position: absolute;
    top: 0;
    left: 0;
    width: 779px;
    height: 600px;
    background:
      radial-gradient(ellipse 260px 330px at 560px 260px, var(--photo-warm) 0%, var(--photo-skin) 45%, rgba(239,198,173,0) 75%),
      linear-gradient(180deg, var(--photo-light) 0%, #ece6e0 100%);
  }
  .wave-edge {
    position: absolute;
    top: 500px;
    left: 0;
    width: 779px;
    height: 140px;
    display: block;
  }
  .offer-panel {
    position: absolute;
    top: 620px;
    left: 0;
    width: 779px;
    height: 580px;
    background: var(--orange);
  }

  .feature-offer {
    position: absolute;
    top: 34px;
    left: 34px;
    width: 300px;
    font-family: "Raleway", sans-serif;
    color: var(--ink);
  }
  .feature-offer .offer-desc {
    font-weight: 500;
    font-size: 17px;
    line-height: 22px;
  }
  .feature-offer .offer-price {
    font-family: "Pinyon Script", cursive;
    font-size: 44px;
    line-height: 52px;
    color: var(--rust);
  }

  .price-list {
    position: absolute;
    top: 170px;
    left: 34px;
    width: 290px;
    list-style: none;
    font-family: "Raleway", sans-serif;
    font-weight: 300;
    font-size: 14px;
    line-height: 18px;
    color: var(--ink);
  }
  .price-list li {
    display: flex;
    justify-content: space-between;
    gap: 10px;
    padding: 4px 0;
    border-bottom: 1px solid rgba(193, 96, 42, 0.35);
  }
  .price-list .price {
    font-weight: 500;
    white-space: nowrap;
  }
  .price-note {
    position: absolute;
    top: 440px;
    left: 34px;
    width: 290px;
    font-family: "Raleway", sans-serif;
    font-weight: 300;
    font-size: 12px;
    line-height: 16px;
    color: var(--ink);
  }

  .headline {
    position: absolute;
    top: 662px;
    left: 0;
    width: 779px;
    text-align: center;
    font-family: "Pinyon Script", cursive;
    font-weight: 400;
    font-size: 70px;
    line-height: 76px;
    color: var(--ink);
  }
  .tagline {
    position: absolute;
    top: 852px;
    left: 0;
    width: 779px;
    text-align: center;
    font-family: "Raleway", sans-serif;
    font-weight: 300;
    font-size: 41px;
    line-height: 50px;
    color: var(--ink);
  }
  .brand-name {
    position: absolute;
    top: 970px;
    left: 0;
    width: 779px;
    text-align: center;
    font-family: "Cinzel", serif;
    font-weight: 600;
    font-size: 50px;
    line-height: 54px;
    letter-spacing: 2px;
    color: var(--ink);
  }
  .salon-info {
    position: absolute;
    top: 1094px;
    left: 0;
    width: 779px;
    text-align: center;
    font-family: "Raleway", sans-serif;
    font-weight: 500;
    font-size: 17px;
    line-height: 22px;
    color: var(--ink);
  }
  .contact-line {
    position: absolute;
    top: 1148px;
    left: 0;
    width: 779px;
    text-align: center;
    font-family: "Raleway", sans-serif;
    font-weight: 300;
    font-size: 15px;
    line-height: 20px;
    color: var(--ink);
  }
</style>
</head>
<body>
  <main class="flyer">
    <div class="hero-photo" role="img" aria-label="Photo of a smiling woman with long wavy blonde hair looking over her bare shoulder, on a white background"></div>

    <div class="feature-offer">
      <p class="offer-desc">Full Head of Foils, Toner, Cut &amp; Blowdry</p>
      <p class="offer-price">$110 every day</p>
    </div>

    <ul class="price-list">
      <li><span>Ladies Cut</span><span class="price">$20</span></li>
      <li><span>Ladies Blowdry</span><span class="price">from $20</span></li>
      <li><span>Mens Cut</span><span class="price">$15</span></li>
      <li><span>Half Head Foils, Toner, Cut &amp; Blowdry</span><span class="price">$80</span></li>
      <li><span>Tint, Cut &amp; Colour</span><span class="price">$60–80</span></li>
      <li><span>Tint, Scattered Foils, Cut &amp; Blowdry</span><span class="price">$70–110</span></li>
      <li><span>Wedding Package Hair &amp; Make up</span><span class="price">$135pp</span></li>
    </ul>
    <p class="price-note">Complete price list on our webpage. Prices subject to change without notice.</p>

    <div class="offer-panel" role="img" aria-label="Orange damask pattern background"></div>

    <svg class="wave-edge" viewBox="0 0 779 140" aria-hidden="true">
      <path d="M0 20 C 180 -10, 420 20, 600 40 C 680 48, 740 50, 779 48 L779 140 L0 140 Z" fill="var(--rust-dark)"/>
      <path d="M0 32 C 180 4, 420 34, 600 56 C 680 64, 740 66, 779 64 L779 140 L0 140 Z" fill="var(--rust)"/>
      <path d="M0 44 C 180 18, 420 48, 600 72 C 680 80, 740 84, 779 84 L779 140 L0 140 Z" fill="var(--orange)"/>
    </svg>

    <h1 class="headline">Look Good,<br>Feel Great</h1>
    <p class="tagline">without paying silly prices</p>

    <p class="brand-name">LUMENCREST<br>SALON</p>

    <p class="salon-info">Private home salon based in Bateau Bay<br>Mobile service provided for weddings only</p>
    <p class="contact-line">P: 0491 826 374 &nbsp;·&nbsp; E: lcs@quorvel.com.au &nbsp;·&nbsp; W: www.lumencrestsalon.com.au</p>
  </main>
</body>
</html>
```